Welcome Series Email: 1st Email in Series BargainLifts.net

I am working to create a three part welcome series email for visitors to my website but I need a little help getting a creative look and feel that looks professional. I am just looking for some help with the design of the 1st email that we can then develop the first email with and pass down some of the creative elements to the next two emails in the series. My site is BargainLifts.net and we sell a broad range of products from motorcycle all the way to wheelchair and mobility so I need to be mindful of all the different customer types. I have a prototype of the 1st email that my email service provider created that is attached and I just am not happy with the design. I would be interested if someone could take the general concept of this email and give it better look. If you have a completely different idea I am open to that as well. The design I choose does not have to be the perfect final product just a great shell that will dictate the look and feel of all emails I send to my customer list.
Thanks for your help!

```html
<!DOCTYPE html>
<html lang="en">
<head>
<meta charset="utf-8">
<title>BargainLifts.net Welcome Email</title>
<link rel="stylesheet" href="https://fonts.googleapis.com/css2?family=Lato:ital,wght@0,400;0,700;0,900;1,900&family=Montserrat:wght@300;400;500&display=swap">
<style>
:root{
  --bar-dark:#4a4a4a;
  --bar-black:#111111;
  --header-bg:#e9e9e9;
  --text-gray:#5f5f5f;
  --text-soft:#9a9a9a;
  --brand-blue:#1d6a9c;
  --panel-blue:#1a84d6;
  --accent-red:#e0121a;
  --icon-gray:#6b6b6b;
  --rule:#cfcfcf;
  --white:#ffffff;
}
*{margin:0;padding:0;box-sizing:border-box}
html,body{width:1200px;height:2351px;overflow:hidden;background:var(--white)}
body{position:relative;font-family:"Lato",sans-serif;color:var(--text-gray)}
.abs{position:absolute}

.topbar{left:0;top:0;width:1200px;height:57px;background:var(--bar-dark);color:#e6e6e6;font-size:21px;display:flex;align-items:center;justify-content:center;gap:14px}
.masthead{left:0;top:57px;width:1200px;height:207px;background:repeating-linear-gradient(135deg,#ececec 0 6px,#e4e4e4 6px 8px);display:flex;align-items:center;justify-content:center}
.brand{display:flex;align-items:center;gap:14px;font-family:"Montserrat",sans-serif;font-weight:500;color:#3d4a5c}
.brand-dot{width:26px;height:26px;border-radius:50%;background:var(--brand-blue)}
.masthead .brand{font-size:52px}

.hero{left:114px;top:277px;width:971px;height:377px;border:1px solid #c9c9c9;overflow:hidden}
.hero-photo{position:absolute;inset:0;background:linear-gradient(180deg,#9fc07a 0%,#6f9a4e 35%,#4a4d50 62%,#3a3c3e 100%)}
.hero-title{position:absolute;left:19px;top:4px;font-weight:900;font-style:italic;font-size:45px;color:var(--white);text-shadow:2px 2px 4px rgba(0,0,0,.6)}
.hero-curve{position:absolute;inset:0}
.offer{position:absolute;left:725px;top:0;width:246px;text-align:center;font-weight:700;color:var(--panel-blue);line-height:1.05}
.offer .red{color:var(--accent-red)}
.offer-free{position:absolute;top:44px;width:100%;font-size:29px;font-weight:900;color:var(--accent-red)}
.offer-ship{position:absolute;top:79px;width:100%;font-size:26px}
.offer-ship span{font-weight:400}
.offer-rule{position:absolute;left:40px;top:150px;width:206px;height:4px;background:var(--panel-blue)}
.offer-carrier{position:absolute;top:170px;width:100%;font-size:29px;font-weight:900}
.offer-price{position:absolute;top:236px;width:100%;font-size:26px;font-weight:400}
.offer-price b{font-weight:900;font-size:30px}
.shop-btn{position:absolute;left:769px;top:278px;width:170px;height:58px;border-radius:6px;background:linear-gradient(180deg,#2d9cf0,#0b5fb8);color:var(--white);font-weight:900;font-size:28px;display:flex;align-items:center;justify-content:center;box-shadow:0 2px 3px rgba(0,0,0,.35);text-shadow:1px 1px 2px rgba(0,0,0,.4)}

.intro{left:0;top:682px;width:1200px;text-align:center;font-family:"Montserrat",sans-serif}
.intro-lead{font-weight:300;font-size:31px;color:#7a7a7a}
.intro-head{font-weight:400;font-size:43px;color:var(--brand-blue);letter-spacing:1.5px;margin-top:4px}

.category{width:225px}
.category-frame{width:225px;height:225px;background:var(--white);box-shadow:0 0 4px rgba(0,0,0,.28);padding:7px}
.category-photo{width:100%;height:100%}
.category-name{margin-top:14px;text-align:center;font-family:"Montserrat",sans-serif;font-size:23px;color:#555}

.dotted-rule{left:114px;top:1446px;width:972px;height:6px;border-top:2px dotted #b5b5b5;border-bottom:2px dotted #b5b5b5}

.member{left:0;top:1480px;width:1200px;text-align:center;font-family:"Montserrat",sans-serif;font-weight:300;font-size:31px;line-height:39px;color:#666}
.promise{left:0;top:1640px;width:1200px;text-align:center;font-family:"Montserrat",sans-serif;font-weight:400;font-size:31px;line-height:39px;color:var(--brand-blue)}

.benefits{left:0;top:1740px;width:1200px;height:258px;background:linear-gradient(180deg,#f7f7f7,#ececec);border-top:1px solid #dedede;border-bottom:1px solid #dedede}
.benefit{position:absolute;top:0;height:258px;text-align:center}
.benefit+.benefit::before{content:"";position:absolute;left:0;top:18px;height:222px;border-left:1px solid #d4d4d4}
.benefit-icon{width:92px;height:92px;border-radius:50%;background:var(--icon-gray);margin:50px auto 0;display:flex;align-items:center;justify-content:center}
.benefit-small{margin-top:28px;font-size:18px;color:#555}
.benefit-big{font-family:"Montserrat",sans-serif;font-size:23px;color:var(--brand-blue);margin-top:2px}

.footer-brand{left:0;top:2036px;width:1200px;display:flex;justify-content:center}
.footer-brand .brand{font-size:36px}
.footer-brand .brand-dot{width:18px;height:18px}
.footer-note{left:0;top:2137px;width:1200px;text-align:center;font-size:21px;line-height:28px;color:#666}
.social{left:0;top:2219px;width:1200px;display:flex;justify-content:center;gap:10px}
.social span{width:43px;height:43px;border-radius:50%;background:var(--icon-gray)}
.copyright{left:0;top:2287px;width:1200px;height:64px;background:var(--bar-black);color:#8a8a8a;font-size:21px;display:flex;align-items:center;justify-content:center}
</style>
</head>
<body>

<div class="abs topbar"><span>Having trouble viewing this email?</span><span>View it in your browser</span></div>

<header class="abs masthead">
  <div class="brand"><span class="brand-dot"></span>BargainLifts.net</div>
</header>

<section class="abs hero">
  <div class="hero-photo" role="img" aria-label="SUV with hitch-mounted carrier and ramp beside a mobility scooter on a driveway, trees behind"></div>
  <div class="hero-title">Affordable Mobility Solutions</div>
  <svg class="hero-curve" width="971" height="377" viewBox="0 0 971 377">
    <path d="M780 0 Q690 188 800 377 L971 377 L971 0 Z" fill="#ffffff" stroke="#1a84d6" stroke-width="5"/>
  </svg>
  <div class="offer">
    <div class="offer-free">FREE SHIPPING</div>
    <div class="offer-ship"><span>on hundreds of</span><br>mobility products!</div>
    <div class="offer-rule"></div>
    <div class="offer-carrier">Wheelchair &amp;<br>Scooter Carriers</div>
    <div class="offer-price">as low as <b class="red">$164.99</b></div>
  </div>
  <div class="shop-btn">SHOP NOW</div>
</section>

<div class="abs intro">
  <p class="intro-lead">See how we are bringing people to new heights with</p>
  <h1 class="intro-head">RAMPS FOR JUST ABOUT ANY OCCASION</h1>
</div>

<div class="abs category" style="left:114px;top:811px"><div class="category-frame"><div class="category-photo" role="img" aria-label="ATV on grass" style="background:linear-gradient(180deg,#8fb25a,#4e5a3a)"></div></div><p class="category-name">Powersport</p></div>
<div class="abs category" style="left:363px;top:811px"><div class="category-frame"><div class="category-photo" role="img" aria-label="Scooter on an aluminium porch ramp" style="background:linear-gradient(180deg,#8d5a45,#a9a9a9)"></div></div><p class="category-name">Mobility</p></div>
<div class="abs category" style="left:613px;top:811px"><div class="category-frame"><div class="category-photo" role="img" aria-label="Forklift with yellow dumpster" style="background:linear-gradient(180deg,#9a9a9a,#e2b21f)"></div></div><p class="category-name">Commercial &amp; Utility</p></div>
<div class="abs category" style="left:863px;top:811px"><div class="category-frame"><div class="category-photo" role="img" aria-label="Red hatchback under blue sky" style="background:linear-gradient(180deg,#5c9ad8,#c8212a)"></div></div><p class="category-name">Automotive</p></div>

<div class="abs category" style="left:114px;top:1135px"><div class="category-frame"><div class="category-photo" role="img" aria-label="Dog running on grass with a toy" style="background:linear-gradient(180deg,#a6bf6a,#6d8c3c)"></div></div><p class="category-name">Pet</p></div>
<div class="abs category" style="left:363px;top:1135px"><div class="category-frame"><div class="category-photo" role="img" aria-label="Cyclist loading a bike rack on a car" style="background:linear-gradient(180deg,#cfd8e0,#5a5e63)"></div></div><p class="category-name">Recreation</p></div>
<div class="abs category" style="left:613px;top:1135px"><div class="category-frame"><div class="category-photo" role="img" aria-label="Utility trailer with loading ramps" style="background:linear-gradient(180deg,#f2f2f2,#6a6a6a)"></div></div><p class="category-name">Trailer</p></div>
<div class="abs category" style="left:863px;top:1135px"><div class="category-frame"><div class="category-photo" role="img" aria-label="Yellow lawn tractor on a metal ramp" style="background:linear-gradient(180deg,#3f4a35,#d6a81c 55%,#9c9c9c)"></div></div><p class="category-name">Home &amp; Garden</p></div>

<div class="abs dotted-rule"></div>

<p class="abs member">As a member of our special email program you will be the<br>first to hear about new products, exclusive offers and<br>upcoming Sales Events.</p>
<p class="abs promise">Our low Prices, fast shipping and 100% money back gurantee<br>truly set us apart in the industry.</p>

<section class="abs benefits">
  <div class="benefit" style="left:114px;width:237px">
    <div class="benefit-icon"><svg width="40" height="50" viewBox="0 0 40 50"><text x="20" y="42" text-anchor="middle" font-family="Lato,sans-serif" font-weight="700" font-size="46" fill="#fff">$</text></svg></div>
    <p class="benefit-small">Quality Products</p><p class="benefit-big">Discount Prices</p>
  </div>
  <div class="benefit" style="left:351px;width:243px">
    <div class="benefit-icon"><svg width="50" height="34" viewBox="0 0 50 34"><rect x="2" y="4" width="28" height="20" fill="#fff"/><path d="M32 10h9l7 8v6H32z" fill="#fff"/><circle cx="12" cy="27" r="5" fill="#fff" stroke="#6b6b6b" stroke-width="2"/><circle cx="38" cy="27" r="5" fill="#fff" stroke="#6b6b6b" stroke-width="2"/></svg></div>
    <p class="benefit-small">Fast</p><p class="benefit-big">Shipping</p>
  </div>
  <div class="benefit" style="left:594px;width:248px">
    <div class="benefit-icon"><svg width="40" height="40" viewBox="0 0 24 24"><path d="M12 2l3 6.6 7.2.7-5.4 4.8 1.6 7.1L12 17.5 5.6 21.2l1.6-7.1L1.8 9.3 9 8.6z" fill="#fff"/></svg></div>
    <p class="benefit-small">Guarantee</p><p class="benefit-big">100% Money Back</p>
  </div>
  <div class="benefit" style="left:842px;width:244px">
    <div class="benefit-icon"><svg width="40" height="40" viewBox="0 0 24 24"><path d="M6.6 10.8a15.2 15.2 0 006.6 6.6l2.2-2.2a1 1 0 011-.25 11.4 11.4 0 003.6.57 1 1 0 011 1V20a1 1 0 01-1 1A17 17 0 013 4a1 1 0 011-1h3.5a1 1 0 011 1c0 1.25.2 2.45.57 3.6a1 1 0 01-.25 1z" fill="#fff"/></svg></div>
    <p class="benefit-small">Call Our Product Experts</p><p class="benefit-big">888-555-0147</p>
  </div>
</section>

<div class="abs footer-brand"><div class="brand"><span class="brand-dot"></span>BargainLifts.net</div></div>
<p class="abs footer-note">You are receiving this email becous you signed up one of<br>our newsletter at Bargain Lifts</p>
<div class="abs social" aria-label="Social links"><span></span><span></span><span></span><span></span><span></span></div>

<footer class="abs copyright">© Copyright 2000-2014 Bargain Lifts All Rights Reserved</footer>

</body>
</html>
```